PACKAGING DESIGN - HOT New Brand of Haircare

We are creating a NEW haircare brand that will need to stand out on retail shelves. This is a luxury product at an affordable price. We will look for designs for 2 different formulas - Shine Boosting Shampoo & Moisturizing Conditioner containing Argan Oil and the other will be a Nourishing Shampoo & Hydrating Conditioner containing Coconut Oil.Packaging will be 32 oz bottle with pump (either Boston Round or Bullet shape). Examples are shown on the brief. This product will be sold at national retailers and needs to look like a brand that is sold at a high end boutique or salon.
Updates

Need extra days to review

Target Market(s)

Women and Men 20s - 40s who want high end hair care

Font styles to use
Sans Serif

Colors

Designer to choose colors to be used in the design.

Requirements
Must have
• Label design for the existing bottle - 4 different SKUs. (see attached brief)

```html
<!DOCTYPE html>
<html lang="en">
<head>
<meta charset="UTF-8">
<title>Solenne – Shine Boosting Shampoo Label</title>
<link rel="stylesheet" href="https://fonts.googleapis.com/css2?family=Roboto+Condensed:wght@300;400;500;700&display=swap">
<style>
  :root {
    --canvas: #ffffff;
    --label-white: #ffffff;
    --ink-grey: #3f4447;
    --ink-dark: #2b3033;
    --brand-orange: #d9782d;
    --teal: #2e9aa3;
    --teal-deep: #1f7f87;
    --teal-soft: #d6ecee;
    --leaf-tone: #a9d3d6;
  }
  html, body {
    margin: 0;
    padding: 0;
    width: 1200px;
    height: 1200px;
    overflow: hidden;
    background: var(--canvas);
    font-family: "Roboto Condensed", "Arial Narrow", sans-serif;
  }
  .label {
    position: absolute;
    left: 230px;
    top: 60px;
    width: 740px;
    height: 1080px;
    background: linear-gradient(to bottom,
      var(--label-white) 0%,
      var(--label-white) 58%,
      var(--teal-soft) 70%,
      var(--teal) 90%,
      var(--teal-deep) 100%);
    box-shadow: 0 0 0 1px #e4e8e9;
  }
  .label > * {
    position: absolute;
    left: 0;
    right: 0;
    text-align: center;
    margin: 0;
    line-height: 1;
  }
  .brand-name {
    top: 150px;
    color: var(--brand-orange);
    font-weight: 400;
    font-size: 104px;
    letter-spacing: 8px;
  }
  .product-title {
    top: 440px;
    color: var(--teal);
    font-weight: 700;
    font-size: 50px;
    letter-spacing: 0.5px;
  }
  .product-type {
    top: 508px;
    color: var(--ink-grey);
    font-weight: 400;
    font-size: 44px;
    letter-spacing: 1px;
  }
  .sprig {
    left: 335px;
    right: auto;
    top: 585px;
    width: 70px;
    height: 95px;
  }
  .key-ingredient {
    top: 704px;
    color: var(--teal);
    font-size: 44px;
    font-weight: 400;
  }
  .hair-type {
    top: 758px;
    color: var(--ink-dark);
    font-size: 36px;
    font-weight: 400;
  }
  .claim-badge {
    left: 215px;
    right: auto;
    top: 806px;
    width: 310px;
    height: 48px;
    line-height: 48px;
    background: var(--brand-orange);
    color: #ffffff;
    font-weight: 700;
    font-size: 26px;
    letter-spacing: 1px;
  }
  .volume {
    top: 950px;
    color: var(--ink-dark);
    font-size: 34px;
    font-weight: 400;
  }
</style>
</head>
<body>
  <main class="label">
    <h1 class="brand-name">SOLENNE</h1>

    <h2 class="product-title">SHINE BOOSTING</h2>
    <p class="product-type">SHAMPOO</p>

    <svg class="sprig" viewBox="0 0 70 95" role="img" aria-label="Small olive sprig ornament">
      <rect x="0" y="0" width="70" height="95" rx="16" fill="var(--leaf-tone)"/>
    </svg>

    <p class="key-ingredient">With Argan Oil</p>
    <p class="hair-type">Dry to normal hair</p>
    <p class="claim-badge">PARABEN -FREE</p>

    <p class="volume">32 fl. oz/ 946 ml</p>
  </main>
</body>
</html>
```